Heron Freightlines needs Bussiness cards!

Our new trucking company needs business cards!
We need the same design with two different names and emails, everything else it's the same.
I have included our original logo so we can use it for the design.
Note: the logo to be used is the o e with the buffalo on the right side, next to the letters H and F.

Target Market(s)

Trucking, refrigerated transportation, freight

Industry/Entity Type

Business

Contact Information for Business Card

Card #1:
Marcus Tellwright
marcustellwright@heronfreightlines.example
1-844-555-0193
(956)555-0178
3817 W. Tarrow Ave.
Pharr, TX 78599
www.heronfreightlines.example

Card#2:
Orla Brennick
orla@heronfreightlines.example
1-844-555-0193
(956)555-0178
3817 W. Tarrow Ave.
Pharr, TX 78599
www.heronfreightlines.example

Font styles to use
Sans Serif

Colors
0655a3
ec1f27
ffffff

Requirements
Must have
• our logo
Nice to have
• roads on background,

```html
<!DOCTYPE html>
<html lang="en">
<head>
<meta charset="utf-8">
<title>Heron Freightlines – Business Card</title>
<link href="https://fonts.googleapis.com/css2?family=Open+Sans:wght@400;600;800&display=swap" rel="stylesheet">
<style>
  :root {
    --backdrop: #3e3935;
    --card: #0e0e0e;
    --card-edge: #1c1c1c;
    --brand-red: #ec1f27;
    --brand-blue: #0655a3;
    --white: #ffffff;
    --text-light: #e6e6e6;
    --silver: #b9b9b9;
  }
  * { box-sizing: border-box; margin: 0; padding: 0; }
  html, body { width: 1200px; height: 900px; overflow: hidden; }
  body {
    background: var(--backdrop);
    font-family: "Open Sans", Arial, sans-serif;
    display: flex;
    align-items: center;
    justify-content: center;
    gap: 60px;
  }
  .card {
    position: relative;
    width: 520px;
    height: 297px;
    background: var(--card);
    border: 1px solid var(--card-edge);
    box-shadow: 0 12px 30px rgba(0,0,0,.45);
  }
  /* Front: contact side */
  .front-brand {
    position: absolute;
    left: 26px;
    top: 168px;
    display: flex;
    align-items: center;
    gap: 8px;
  }
  .brand-dot {
    width: 12px; height: 12px;
    border-radius: 50%;
    background: var(--brand-blue);
  }
  .front-brand .brand-name {
    font-weight: 800;
    font-size: 19px;
    color: var(--brand-red);
    letter-spacing: -.2px;
  }
  .divider {
    position: absolute;
    left: 232px;
    top: 40px;
    width: 1px;
    height: 185px;
    background: linear-gradient(var(--brand-red), rgba(236,31,39,.15));
  }
  .contact {
    position: absolute;
    left: 246px;
    top: 36px;
    right: 14px;
    color: var(--text-light);
  }
  .contact-name {
    font-weight: 600;
    font-size: 15px;
    color: var(--brand-red);
    margin-bottom: 18px;
  }
  .address { font-size: 12px; line-height: 17px; margin-bottom: 18px; }
  .contact-list { list-style: none; font-size: 11px; line-height: 18px; }
  .contact-list li { display: flex; align-items: center; gap: 8px; white-space: nowrap; }
  .contact-list svg { width: 9px; height: 9px; flex: none; fill: var(--brand-red); }
  /* Back: brand side */
  .back {
    display: flex;
    align-items: center;
    justify-content: center;
  }
  .back .brand-name {
    font-weight: 800;
    font-size: 40px;
    color: var(--silver);
    letter-spacing: -.5px;
  }
</style>
</head>
<body>
  <section class="card front">
    <div class="front-brand">
      <span class="brand-dot"></span>
      <span class="brand-name">Heron Freightlines</span>
    </div>
    <div class="divider"></div>
    <div class="contact">
      <p class="contact-name">Marcus Tellwright</p>
      <p class="address">3817 W. Tarrow Ave.<br>Pharr, TX 78599</p>
      <ul class="contact-list">
        <li><svg viewBox="0 0 10 10"><rect x="2.5" y="0" width="5" height="10" rx="1"/></svg>(956)555-0178</li>
        <li><svg viewBox="0 0 10 10"><path d="M2 0l2 2-1 2 3 3 2-1 2 2-2 2C4 10 0 6 0 2z"/></svg>1-844-555-0193</li>
        <li><svg viewBox="0 0 10 10"><path d="M0 2h10v6H0z M0 2l5 3 5-3"/></svg>marcustellwright@heronfreightlines.example</li>
        <li><svg viewBox="0 0 10 10"><circle cx="5" cy="5" r="5"/></svg>www.heronfreightlines.example</li>
      </ul>
    </div>
  </section>
  <section class="card back">
    <span class="brand-name">Heron Freightlines</span>
  </section>
</body>
</html>
```